South Carolina Bridal and Formal Wear Store

We want The Gown Parlor of Ashcombe website to feel luxurious, elegant, welcoming, and approachable—without feeling overpriced or intimidating. The site should immediately show that we are a full-service bridal and formal wear destination, offering bridal gowns, prom, mothers’ dresses, tuxedos and suits, accessories, and more. We want beautiful, high-end imagery and a clean, modern design while still reflecting the warm, personal experience customers receive when they walk into our boutique. Most importantly, the website should be easy to shop and navigate, allowing customers to browse our collections, see what we offer, understand price ranges, book appointments, and feel excited and comfortable choosing The Gown Parlor of Ashcombe for all of their special-event needs.

Target Market(s)

Women ages 18-50. Brides, engaged women, mothers of the occasion

Industry/Entity Type

Bridal and Formal Wear

Coding

Coded - Design and coding required

Number of Pages Required

5+ page

Font styles to use
Sans Serif

Colors

Designer to choose colors to be used in the design.

Requirements
Must have
• Appointment area, about us staff area, what we offer and designers our logo
Nice to have
• Modern Southern Luxury: Clean, elegant, and upscale with soft neutral tones, beautiful bridal photography, and a warm Lowcountry feel.
Should not have
• pricing

```html
<!DOCTYPE html>
<html lang="en">
<head>
<meta charset="utf-8">
<title>The Gown Parlor of Ashcombe — Collections</title>
<link rel="stylesheet" href="https://fonts.googleapis.com/css2?family=Jost:wght@400;500&family=Inter:wght@400;500&display=swap">
<style>
:root{
  --ink:#2e1f28;
  --plum:#2e1f28;
  --cream:#faf7f2;
  --sand:#f3e9e0;
  --gold:#b8956a;
  --text:#4a3d44;
  --white:#ffffff;
}
*{box-sizing:border-box;margin:0;padding:0}
html,body{width:1200px;height:2880px;overflow:hidden}
body{background:var(--white);font-family:"Inter",Arial,sans-serif;color:var(--text)}
.wrap{width:750px;margin:0 auto}

/* header */
.site-header{height:90px;background:var(--cream);border-bottom:1px solid #ece4da}
.site-header .wrap{height:100%;display:flex;align-items:center;justify-content:space-between}
.brand{font-family:"Jost",sans-serif;font-weight:400;font-size:19px;color:var(--ink);width:200px;line-height:1.2}
.main-nav{display:flex;gap:24px;font-family:"Jost",sans-serif;font-size:9.5px;letter-spacing:.8px;color:var(--ink)}
.main-nav .active{border-bottom:1px solid var(--gold);padding-bottom:4px}
.btn{display:inline-block;background:var(--plum);color:var(--white);font-family:"Jost",sans-serif;font-size:9.5px;padding:10px 22px;letter-spacing:.3px}

/* hero */
.hero{height:304px;position:relative;background:linear-gradient(100deg,#5a6b4a 0%,#7b8466 40%,#8d8a7c 60%,#5f6a4e 100%)}
.hero::after{content:"";position:absolute;inset:0;background:rgba(30,20,26,.35)}
.hero .wrap{position:relative;z-index:1;padding-top:122px}
.eyebrow{font-family:"Jost",sans-serif;font-size:8.5px;letter-spacing:3px;text-transform:uppercase;color:var(--gold)}
.hero .eyebrow{color:var(--white);font-size:9.5px}
.hero h1{font-family:"Jost",sans-serif;font-weight:400;font-size:39px;color:var(--white);margin-top:6px}

.sub-nav{height:33px;background:var(--sand);display:flex;justify-content:center;align-items:center;gap:21px;font-family:"Jost",sans-serif;font-size:9.5px;letter-spacing:1px;color:var(--ink)}

/* collection rows */
.collection{height:325px}
.collection--sand{background:var(--sand)}
.collection--plum{background:var(--plum)}
.collection .wrap{height:100%;display:flex;align-items:center;justify-content:space-between}
.collection--reverse .wrap{flex-direction:row-reverse}
.photo-pair{display:flex;gap:10px;width:358px;height:205px}
.photo{width:174px;height:180px;box-shadow:0 6px 14px rgba(0,0,0,.12)}
.photo--low{margin-top:25px}
.copy{width:358px}
.collection h2{font-family:"Jost",sans-serif;font-weight:400;font-size:24px;line-height:1.2;color:var(--ink);margin-top:10px}
.rule{width:40px;height:1px;background:var(--gold);margin:18px 0 20px}
.copy p{font-size:10px;line-height:1.65;color:var(--text)}
.copy .link{display:block;margin-top:18px;font-family:"Jost",sans-serif;font-size:9px;letter-spacing:1px;color:var(--ink)}
.collection--plum h2,.collection--plum p,.collection--plum .link{color:var(--white)}

/* preservation */
.preserve{height:285px;text-align:center;padding-top:64px}
.preserve h2{font-family:"Jost",sans-serif;font-weight:400;font-size:24px;color:var(--ink);margin-top:9px}
.preserve .rule{margin:14px auto 16px}
.preserve p{font-size:10px;line-height:1.65;width:420px;margin:0 auto 20px}
.preserve .btn{font-size:10px;padding:11px 23px}

/* footer */
.site-footer{height:218px;background:var(--plum);color:#e9dfe3;position:relative}
.footer-cols{display:flex;padding-top:40px}
.footer-col{width:194px;font-size:9px;line-height:1.5}
.footer-col:last-child{width:168px}
.footer-col h4{font-family:"Jost",sans-serif;font-weight:400;font-size:8.5px;letter-spacing:1px;color:var(--gold);margin-bottom:12px}
.footer-col ul{list-style:none}
.footer-col li{margin-bottom:7px}
.footer-brand{font-family:"Jost",sans-serif;font-size:15px;color:var(--white);margin-bottom:12px;line-height:1.2}
.hours{display:flex;justify-content:space-between;margin-bottom:4px}
.footer-bar{position:absolute;left:0;right:0;bottom:0;height:40px;border-top:1px solid #46363f}
.footer-bar .wrap{height:100%;display:flex;align-items:center;justify-content:space-between;font-size:8px;color:#b7a9b0}
</style>
</head>
<body>
<header class="site-header">
  <div class="wrap">
    <div class="brand">The Gown Parlor of Ashcombe</div>
    <nav class="main-nav">
      <span>HOME</span><span>ABOUT</span><span class="active">COLLECTIONS</span><span>APPOINTMENTS</span><span>FAQ</span><span>CONTACT</span>
    </nav>
    <span class="btn">Book an Appointment</span>
  </div>
</header>

<section class="hero" role="img" aria-label="Bride with a lace parasol and groom outdoors beside a vintage green truck under mossy oaks">
  <div class="wrap">
    <div class="eyebrow">Collections</div>
    <h1>Something beautiful for every occasion</h1>
  </div>
</section>

<nav class="sub-nav">
  <span>BRIDAL</span><span>BRIDESMAIDS</span><span>MOTHERS</span><span>TUXEDOS &amp; SUITS</span><span>PROM</span><span>ACCESSORIES</span><span>GOWN PRESERVATION</span>
</nav>

<section class="collection">
  <div class="wrap">
    <div class="photo-pair">
      <div class="photo photo--low" role="img" aria-label="Bride in a strapless ivory ball gown in an ornate room" style="background:linear-gradient(160deg,#8a6a44,#d9cfc2 70%,#efe9e1)"></div>
      <div class="photo" role="img" aria-label="Bride in a strapless gown by a tall window" style="background:linear-gradient(160deg,#b99a6e,#e8e0d4 60%,#f3eee7)"></div>
    </div>
    <div class="copy">
      <div class="eyebrow">Bridal Gowns</div>
      <h2>Find the gown that feels like you</h2>
      <div class="rule"></div>
      <p>From romantic lace to sleek modern silhouettes, our curated bridal collection features designers including Julian Ashford, Maribelle, Tessa Orlund, and Willowmere Bridal Collection. Our stylists will guide you through fabrics, necklines, and details to help you discover the dress that feels unmistakably you.</p>
      <span class="link">BOOK A BRIDAL APPOINTMENT →</span>
    </div>
  </div>
</section>

<section class="collection collection--sand collection--reverse">
  <div class="wrap">
    <div class="photo-pair">
      <div class="photo" role="img" aria-label="Couple embracing beside a white wall with black framed windows" style="background:linear-gradient(160deg,#f2f1ee,#d9d8d4 60%,#b9b7b2)"></div>
      <div class="photo photo--low" role="img" aria-label="Bride from behind holding a bouquet near wooden doors" style="background:linear-gradient(160deg,#e8e6e2,#cfc7bc 50%,#9c7a58)"></div>
    </div>
    <div class="copy">
      <div class="eyebrow">Bridesmaids</div>
      <h2>Coordinated style for your whole crew</h2>
      <div class="rule"></div>
      <p>Outfit your bridal party in coordinating styles and colors from Maribelle, Delaney Collection, Arden Soule, Half Past Eight, and Lark &amp; Lace Bridesmaids. Mix and match silhouettes to flatter every member of your party while keeping a cohesive look.</p>
      <span class="link">BOOK A BRIDESMAID APPOINTMENT →</span>
    </div>
  </div>
</section>

<section class="collection">
  <div class="wrap">
    <div class="photo-pair">
      <div class="photo photo--low" role="img" aria-label="Stylist adjusting a bride's train among gown racks" style="background:linear-gradient(160deg,#e6e2dc,#c9bfb3 60%,#7a5a3e)"></div>
      <div class="photo" role="img" aria-label="Stylist placing a lace veil on a bride" style="background:linear-gradient(160deg,#d8d2cb,#8a7566 55%,#e4ded8)"></div>
    </div>
    <div class="copy">
      <div class="eyebrow">Mother of the Occasion</div>
      <h2>Elegant looks for the mothers of the day</h2>
      <div class="rule"></div>
      <p>We carry sophisticated, comfortable pieces from MVRL, Marbella Rose, Arden Soule, and Half Past Eight so every mother of the occasion feels beautiful and confident.</p>
      <span class="link">BOOK A MOTHERS APPOINTMENT →</span>
    </div>
  </div>
</section>

<section class="collection collection--plum collection--reverse">
  <div class="wrap">
    <div class="photo-pair">
      <div class="photo" role="img" aria-label="Groom in a tuxedo with bride beside white clapboard siding" style="background:linear-gradient(160deg,#dcdad6,#4f5a3c 45%,#efece8)"></div>
      <div class="photo photo--low" role="img" aria-label="Couple walking down a path under live oaks" style="background:linear-gradient(160deg,#4b5a3a,#7d8a64 50%,#cfd2c2)"></div>
    </div>
    <div class="copy">
      <div class="eyebrow">Tuxedos &amp; Suits</div>
      <h2>Sharp, tailored looks for the groom &amp; groomsmen</h2>
      <div class="rule"></div>
      <p>We love our guys! Choose from tuxedos and suits for rent or purchase through Hollis Formal Wear and Carrow's Formal Wear. Book a tuxedo appointment for measurements, or call us in for out-of-town groomsmen — we also offer direct shipping.</p>
      <span class="link">BOOK A TUXEDO APPOINTMENT →</span>
    </div>
  </div>
</section>

<section class="collection">
  <div class="wrap">
    <div class="photo-pair">
      <div class="photo photo--low" role="img" aria-label="Woman in a blush tulle gown on brick steps with flowers" style="background:linear-gradient(160deg,#6f7a5c,#f1d9cf 55%,#a9563f)"></div>
      <div class="photo" role="img" aria-label="Black and white photo of a couple beneath a large oak" style="background:linear-gradient(160deg,#d9d9d9,#8c8c8c 55%,#e4e4e4)"></div>
    </div>
    <div class="copy">
      <div class="eyebrow">Prom &amp; Formal Wear</div>
      <h2>Show-stopping looks for prom night</h2>
      <div class="rule"></div>
      <p>From bold colors to classic silhouettes, our prom collection has something for every style. Our stylists will help you find a look that turns heads all night long.</p>
      <span class="link">BOOK A PROM APPOINTMENT →</span>
    </div>
  </div>
</section>

<section class="collection collection--sand collection--reverse">
  <div class="wrap">
    <div class="photo-pair">
      <div class="photo" role="img" aria-label="Couple standing under a draped brick archway" style="background:linear-gradient(160deg,#6e5038,#e5e1dc 60%,#3e3a33)"></div>
      <div class="photo photo--low" role="img" aria-label="Bride with a long veil at a railing over the marsh at sunset" style="background:linear-gradient(180deg,#ead8c6,#8f8a6a 45%,#2e2a26 70%,#e8e4de)"></div>
    </div>
    <div class="copy">
      <div class="eyebrow">Accessories</div>
      <h2>The finishing touches</h2>
      <div class="rule"></div>
      <p>Veils, belts, jewelry and more — complete your look with accessories hand-selected to complement your gown.</p>
    </div>
  </div>
</section>

<section class="preserve">
  <div class="eyebrow">Wedding Gown Preservation</div>
  <h2>Keep your gown beautiful for a lifetime</h2>
  <div class="rule"></div>
  <p>We are an authorized retailer for the Heirloom Gown Care Company and also offer on-site steaming. Leave preserving your gown to us — contact us for more details.</p>
  <span class="btn">Contact Us</span>
</section>

<footer class="site-footer">
  <div class="wrap footer-cols">
    <div class="footer-col">
      <div class="footer-brand">The Gown Parlor of Ashcombe</div>
      <p>A full-service bridal &amp; formal wear boutique bringing modern Southern luxury to Ashcombe, SC.</p>
    </div>
    <div class="footer-col">
      <h4>EXPLORE</h4>
      <ul><li>About Us</li><li>Collections</li><li>Appointments</li><li>FAQ</li></ul>
    </div>
    <div class="footer-col">
      <h4>VISIT US</h4>
      <p>2240 Marsh Hen Lane, Suite 12<br>Ashcombe, SC 29000</p>
      <p style="margin-top:8px">555-014-2290</p>
      <p style="margin-top:8px">hello@gownparlorashcombe.example</p>
    </div>
    <div class="footer-col">
      <h4>STORE HOURS</h4>
      <div class="hours"><span>Sun – Tue</span><span>Closed</span></div>
      <div class="hours"><span>Wed – Sat</span><span>10am – 6pm</span></div>
    </div>
  </div>
  <div class="footer-bar">
    <div class="wrap">
      <span>© 2026 The Gown Parlor of Ashcombe. All rights reserved.</span>
      <span>Bridal · Tuxedos · Formal Wear · Ashcombe, SC</span>
    </div>
  </div>
</footer>
</body>
</html>
```